Social Media designs (LinkedIn banner, LinkedIn posts, Instagram)

Hello designers!
We are looking to create some more concepts for our social media identity for a search firm (recruitment company)
I have attached a "brand toolkit" that shows our brand, logo, colour scheme to guide you with regards to colours and identiy.

You will see in the brand toolkit there are some examples of;
- A LinkedIn banner for the company (page 23)
- Social Media posts for LinkedIn and Instagram (page 21)

What we are looking for...

We don't really like the current LinkedIn banner ideas. We would like to see more concepts that look more aesthetically pleasing - the current ideas look quite dull.

We DO like the social media post concepts but we would like to have more templates/options that we can use (similar themes)

We welcome submissions for Social Media designs that we can use with our company branding. Thank you for your work in advance!

```html
<!DOCTYPE html>
<html lang="en">
<head>
<meta charset="utf-8">
<title>Marlow Reeve – Social Media Concepts</title>
<link rel="stylesheet" href="https://fonts.googleapis.com/css2?family=Outfit:wght@300;400;600;700&display=swap">
<style>
  :root {
    --ink: #16302b;
    --deep: #142925;
    --green: #3f8a63;
    --mint: #8fc1a5;
    --white: #ffffff;
    --paper: #fafafa;
    --muted: #6f8f80;
  }
  * { box-sizing: border-box; margin: 0; padding: 0; }
  html, body { width: 1200px; height: 1200px; overflow: hidden; background: var(--white); }
  body { position: relative; font-family: "Outfit", sans-serif; color: var(--ink); }

  .label { position: absolute; font-weight: 700; font-size: 39px; line-height: 1; letter-spacing: -0.3px; color: var(--ink); }
  .label--banner-1 { right: 134px; top: 54px; }
  .label--banner-2 { right: 138px; top: 366px; }
  .label--post-1 { left: 178px; top: 703px; }
  .label--post-2 { left: 826px; top: 708px; }
  .section-title--banner {
    position: absolute; left: 132px; top: 604px; transform-origin: left top; transform: rotate(-90deg);
    font-weight: 700; font-size: 60px; line-height: 1; white-space: nowrap; letter-spacing: -0.3px;
  }
  .section-title--posts {
    position: absolute; left: 453px; top: 858px; width: 300px; text-align: center;
    font-weight: 700; font-size: 39px; line-height: 1;
  }

  .banner { position: absolute; overflow: hidden; }
  .banner--v1 { left: 238px; top: 111px; width: 830px; height: 208px; }
  .banner--v2 { left: 235px; top: 426px; width: 833px; height: 209px; background: var(--ink); }
  .banner__photo { position: absolute; inset: 0; }
  .banner--v1 .banner__photo { background: linear-gradient(100deg, #0f1e1b 0%, #1b2e2a 40%, #121d1b 62%, #4a5a55 78%, #8a8f8d 100%); }
  .banner--v1 .banner__bands { position: absolute; inset: 0; }
  .banner__strip { position: absolute; left: 0; bottom: 0; width: 500px; height: 11px; background: var(--green); opacity: .85; }
  .banner--v2 .banner__photo { left: 549px; background: linear-gradient(90deg, #5f9a80 0%, #3c6b58 35%, #1e3b33 70%, #2c4a41 100%); }

  .banner__headline { position: absolute; font-weight: 700; color: var(--white); line-height: 1.03; }
  .banner--v1 .banner__headline { left: 207px; top: 62px; font-size: 40px; letter-spacing: -0.5px; }
  .banner--v2 .banner__headline { left: 205px; top: 67px; font-size: 41px; font-weight: 600; letter-spacing: -0.3px; }
  .accent { color: var(--green); }

  .brand-tile {
    position: absolute; width: 136px; height: 135px; background: var(--ink);
    border: 5px solid var(--white); outline: 1px solid #d8dedc;
    display: flex; align-items: center; justify-content: center; text-align: center;
    color: var(--white); font-weight: 600; font-size: 22px; line-height: 1.05;
  }
  .brand-tile--v1 { left: 261px; top: 205px; }
  .brand-tile--v2 { left: 261px; top: 521px; }

  .post { position: absolute; width: 300px; background: var(--white); box-shadow: 0 2px 10px rgba(0,0,0,.08); border-radius: 8px 8px 0 0; overflow: hidden; }
  .post--v1 { left: 128px; top: 765px; height: 380px; }
  .post--v2 { left: 779px; top: 770px; height: 380px; }
  .post__header { height: 43px; display: flex; align-items: center; padding: 0 10px; gap: 8px; font-size: 10px; font-weight: 600; color: #222; }
  .post__avatar { width: 24px; height: 24px; border-radius: 50%; background: var(--ink); }
  .post__more { margin-left: auto; font-size: 14px; letter-spacing: 1px; }
  .post__media { position: relative; width: 300px; height: 300px; overflow: hidden; }
  .post__actions { height: 37px; display: flex; align-items: center; padding: 0 9px; gap: 14px; }
  .post__actions svg { width: 20px; height: 20px; fill: none; stroke: #222; stroke-width: 1.5; }
  .post__actions .save { margin-left: auto; }

  .post--v1 .panel { position: absolute; left: 0; top: 0; width: 127px; height: 300px; background: linear-gradient(180deg, #21352f 0%, #1a302a 60%, #1f3a32 100%); }
  .post--v1 .scene { position: absolute; left: 127px; top: 0; right: 0; bottom: 0; background: linear-gradient(160deg, #3b4a4d 0%, #1a2426 40%, #3c3a36 65%, #232a2b 100%); }
  .post--v1 .frame { position: absolute; left: 0; top: 0; width: 300px; height: 300px; }
  .wordmark { position: absolute; color: var(--white); font-weight: 400; font-size: 13px; line-height: 1; }
  .post--v1 .wordmark { left: 9px; top: 9px; }
  .post--v1 .wordmark::before { content: ""; display: inline-block; width: 14px; height: 14px; background: var(--green); vertical-align: -2px; margin-right: 5px; }
  .report-title { position: absolute; left: 7px; top: 68px; color: var(--white); font-weight: 700; font-size: 17px; line-height: 1; letter-spacing: -0.4px; }
  .report-copy { position: absolute; left: 0; top: 143px; width: 127px; height: 104px; background: var(--white); padding: 22px 6px 0 7px; font-size: 10.5px; line-height: 1.1; color: var(--ink); font-weight: 300; }
  .cta { position: absolute; font-size: 7.5px; line-height: 1.05; color: var(--white); }
  .cta span { display: block; color: var(--muted); }
  .post--v1 .cta { left: 9px; top: 276px; }

  .post--v2 .scene { position: absolute; inset: 0; background: radial-gradient(ellipse at 40% 40%, #2c3b35 0%, #1a2a25 55%, #132520 100%); }
  .post--v2 .arcs { position: absolute; inset: 0; }
  .post--v2 .wordmark { left: 0; right: 0; top: 20px; text-align: center; font-size: 14px; }
  .post--v2 .wordmark::before { content: ""; display: inline-block; width: 15px; height: 15px; background: var(--green); vertical-align: -2px; margin-right: 6px; }
  .post-headline { position: absolute; left: 0; right: 0; top: 134px; text-align: center; color: var(--white); font-weight: 700; font-size: 22px; line-height: .95; letter-spacing: -0.4px; }
  .post-headline .rule { display: block; width: 100px; height: 3px; background: var(--green); margin: 3px auto 0; }
  .post--v2 .cta { left: 0; right: 0; top: 270px; text-align: center; }
</style>
</head>
<body>

<h2 class="section-title--banner">LinkedIn Banner</h2>

<div class="label label--banner-1">Variation 1</div>
<section class="banner banner--v1">
  <div class="banner__photo" role="img" aria-label="Dark city architecture with a church dome, fading into an empty street between old buildings"></div>
  <svg class="banner__bands" viewBox="0 0 830 208" preserveAspectRatio="none" aria-hidden="true">
    <polygon points="570,0 600,0 680,208 645,208" fill="#3f8a63" opacity=".55"/>
    <polygon points="755,0 800,0 830,60 830,120" fill="#3f8a63" opacity=".5"/>
    <polygon points="830,150 780,208 830,208" fill="#3f8a63" opacity=".4"/>
  </svg>
  <div class="banner__strip"></div>
  <h1 class="banner__headline"><span class="accent">TALENT</span> KNOWS<br>NO BORDERS</h1>
</section>
<div class="brand-tile brand-tile--v1">Marlow<br>Reeve</div>

<div class="label label--banner-2">Variation 2</div>
<section class="banner banner--v2">
  <div class="banner__photo" role="img" aria-label="Green-tinted cathedral dome and glass tower facade"></div>
  <h1 class="banner__headline">Talent knows<br>no borders</h1>
</section>
<div class="brand-tile brand-tile--v2">Marlow<br>Reeve</div>

<div class="label label--post-1">Variation 1</div>
<div class="label label--post-2">Variation 2</div>
<h2 class="section-title--posts">Social Media Posts</h2>

<article class="post post--v1">
  <header class="post__header"><span class="post__avatar"></span>marlowreeve<span class="post__more">•••</span></header>
  <div class="post__media">
    <div class="panel" role="img" aria-label="Dark green-tinted office tower"></div>
    <div class="scene" role="img" aria-label="Elevated train passing curved glass towers at dusk"></div>
    <svg class="frame" viewBox="0 0 300 300" aria-hidden="true">
      <polyline points="131,10 282,10 282,286 131,286" fill="none" stroke="#3f8a63" stroke-width="1.5"/>
    </svg>
    <div class="wordmark">Marlow Reeve</div>
    <h3 class="report-title">Q2 2023<br>EXEC HIRING<br>REPORT</h3>
    <p class="report-copy">We’ve pulled together all the data and trends from Q2, along with what to watch out for in Q3.</p>
    <p class="cta"><span>Find out more at</span>marlowreeve.com</p>
  </div>
  <footer class="post__actions">
    <svg viewBox="0 0 24 24"><path d="M12 20s-8-5-8-11a4.5 4.5 0 0 1 8-2.5A4.5 4.5 0 0 1 20 9c0 6-8 11-8 11z"/></svg>
    <svg viewBox="0 0 24 24"><path d="M20 12a8 8 0 1 1-3-6.2A8 8 0 0 1 20 12l1 8-5-2.5"/></svg>
    <svg viewBox="0 0 24 24"><path d="M3 4h18L11 13zM11 13l3 8 7-17"/></svg>
    <svg class="save" viewBox="0 0 24 24"><path d="M6 3h12v18l-6-5-6 5z"/></svg>
  </footer>
</article>

<article class="post post--v2">
  <header class="post__header"><span class="post__avatar"></span>marlowreeve<span class="post__more">•••</span></header>
  <div class="post__media">
    <div class="scene" role="img" aria-label="Dark green-tinted stone bridge with ornate lamp posts and a statue column"></div>
    <svg class="arcs" viewBox="0 0 300 300" aria-hidden="true">
      <path d="M80 300 A220 220 0 0 1 300 80" fill="none" stroke="#3f8a63" stroke-width=".8" opacity=".5"/>
      <path d="M150 300 A150 150 0 0 1 300 150" fill="none" stroke="#3f8a63" stroke-width=".8" opacity=".4"/>
    </svg>
    <div class="wordmark">Marlow Reeve</div>
    <h3 class="post-headline"><span class="accent">TALENT</span> KNOWS<br>NO BORDERS<span class="rule"></span></h3>
    <p class="cta"><span>Find out more at</span>marlowreeve.com</p>
  </div>
  <footer class="post__actions">
    <svg viewBox="0 0 24 24"><path d="M12 20s-8-5-8-11a4.5 4.5 0 0 1 8-2.5A4.5 4.5 0 0 1 20 9c0 6-8 11-8 11z"/></svg>
    <svg viewBox="0 0 24 24"><path d="M20 12a8 8 0 1 1-3-6.2A8 8 0 0 1 20 12l1 8-5-2.5"/></svg>
    <svg viewBox="0 0 24 24"><path d="M3 4h18L11 13zM11 13l3 8 7-17"/></svg>
    <svg class="save" viewBox="0 0 24 24"><path d="M6 3h12v18l-6-5-6 5z"/></svg>
  </footer>
</article>

</body>
</html>
```